NovaLumaro Unique Gift Certificate

We need a unique, luxury gift certificate created for our online company (NovaLumaro). We are looking for something out of the ordinary, ie. do not want it to look like a 'normal' gift certificate. Please visit our website to gain a feel for our company (novalumaro.com.au). The dimensions are 148x148mm. We need our logo, website details, to, from, description, code, exp date included. The certificate will be printed on wood veneer so watermarks will not work. We want it to be clean and minimalistic.

Industry/Entity Type

It Company

```html
<!DOCTYPE html>
<html lang="en">
<head>
<meta charset="utf-8">
<title>NovaLumaro Gift Certificate</title>
<link rel="stylesheet" href="https://fonts.googleapis.com/css2?family=Montserrat:wght@600;800&family=Quicksand:wght@300;500&display=swap">
<style>
  :root {
    --ink: #111111;
    --ink-soft: #3a3a3a;
    --brand-blue: #1f9fd0;
    --rule-blue: #3aa7e0;
    --paper: #ffffff;
  }
  html, body {
    margin: 0;
    padding: 0;
    overflow: hidden;
    background: var(--paper);
  }
  .certificate {
    position: relative;
    width: 1200px;
    height: 1200px;
    overflow: hidden;
    background: var(--paper);
    color: var(--ink);
  }

  /* Brand name */
  .brand {
    position: absolute;
    left: 73px;
    top: 250px;
    width: 300px;
    margin: 0;
    text-align: center;
    font-family: "Quicksand", sans-serif;
    font-weight: 500;
    font-size: 44px;
    letter-spacing: 0.5px;
    line-height: 1;
    color: var(--ink-soft);
  }

  /* Photo mosaic */
  .mosaic {
    position: absolute;
    left: 0;
    top: 0;
  }

  /* Vertical title */
  .title {
    position: absolute;
    bottom: 187px;
    margin: 0;
    writing-mode: vertical-rl;
    transform: rotate(180deg);
    line-height: 1;
    color: var(--ink);
  }
  .title-gift {
    left: 912px;
    font-family: "Montserrat", sans-serif;
    font-weight: 800;
    font-size: 104px;
    letter-spacing: -2px;
  }
  .title-certificate {
    left: 1008px;
    font-family: "Quicksand", sans-serif;
    font-weight: 300;
    font-size: 124px;
    letter-spacing: 1px;
  }

  /* Fields */
  .fields {
    position: absolute;
    left: 73px;
    top: 618px;
    width: 527px;
    margin: 0;
    padding: 0;
    list-style: none;
  }
  .field {
    display: flex;
    align-items: baseline;
    height: 83.5px;
    font-family: "Montserrat", sans-serif;
    font-weight: 600;
    font-size: 27px;
  }
  .field-label {
    flex: none;
  }
  .field-line {
    flex: 1;
    margin-left: 4px;
    border-bottom: 2px dotted var(--rule-blue);
    transform: translateY(-2px);
  }

  /* Tagline band */
  .band {
    position: absolute;
    left: 73px;
    top: 1049px;
    width: 1054px;
    height: 60px;
    box-sizing: border-box;
    padding: 0 24px;
    display: flex;
    align-items: center;
    justify-content: space-between;
    background: var(--brand-blue);
    color: var(--paper);
    font-family: "Quicksand", sans-serif;
    font-weight: 500;
    font-size: 22px;
  }
  .band-text {
    flex: 1;
    text-align: left;
    padding-left: 28px;
  }
  .band-text strong {
    font-family: "Montserrat", sans-serif;
    font-weight: 800;
    font-style: italic;
    font-size: 19px;
  }

  .website {
    position: absolute;
    left: 0;
    width: 1200px;
    top: 1126px;
    margin: 0;
    text-align: center;
    font-family: "Montserrat", sans-serif;
    font-weight: 600;
    font-size: 25px;
    letter-spacing: 2px;
    color: var(--ink);
  }
</style>
</head>
<body>
<main class="certificate">

  <p class="brand">novalumaro</p>

  <svg class="mosaic" width="1200" height="640" viewBox="0 0 1200 640">
    <defs>
      <linearGradient id="sunset-lake" x1="0" y1="0" x2="0" y2="1">
        <stop offset="0" stop-color="#f6cf7a"/><stop offset="1" stop-color="#b89270"/>
      </linearGradient>
      <linearGradient id="reef-dive" x1="0" y1="0" x2="0" y2="1">
        <stop offset="0" stop-color="#4a9aa6"/><stop offset="1" stop-color="#123f46"/>
      </linearGradient>
      <linearGradient id="meadow-walk" x1="0" y1="0" x2="0" y2="1">
        <stop offset="0" stop-color="#b7d2e6"/><stop offset="1" stop-color="#6f9a48"/>
      </linearGradient>
      <linearGradient id="flower-light" x1="0" y1="0" x2="1" y2="1">
        <stop offset="0" stop-color="#f6efe2"/><stop offset="1" stop-color="#cdb79c"/>
      </linearGradient>
      <linearGradient id="massage-calm" x1="0" y1="0" x2="0" y2="1">
        <stop offset="0" stop-color="#7f9c68"/><stop offset="1" stop-color="#ece2d6"/>
      </linearGradient>
      <linearGradient id="autumn-glow" x1="0" y1="0" x2="1" y2="1">
        <stop offset="0" stop-color="#f6b04a"/><stop offset="1" stop-color="#b3452a"/>
      </linearGradient>
      <linearGradient id="jungle-hike" x1="0" y1="0" x2="0" y2="1">
        <stop offset="0" stop-color="#d5dfd5"/><stop offset="1" stop-color="#3f6b5a"/>
      </linearGradient>
      <linearGradient id="beach-sunrise" x1="0" y1="0" x2="0" y2="1">
        <stop offset="0" stop-color="#f8d7a8"/><stop offset="1" stop-color="#ebe6df"/>
      </linearGradient>
      <linearGradient id="lake-yoga" x1="0" y1="0" x2="0" y2="1">
        <stop offset="0" stop-color="#9dbcae"/><stop offset="1" stop-color="#3a685d"/>
      </linearGradient>
      <linearGradient id="harvest-basket" x1="0" y1="0" x2="1" y2="1">
        <stop offset="0" stop-color="#d9503c"/><stop offset="1" stop-color="#7c9a3c"/>
      </linearGradient>
    </defs>

    <g role="img" aria-label="Photo: woman sitting by a lake at sunset">
      <polygon fill="url(#sunset-lake)" points="799,160 753,240 661,240 615,160 661,80 753,80"/>
    </g>
    <g role="img" aria-label="Photo: diver swimming above a sea turtle">
      <polygon fill="url(#reef-dive)" points="959,73 913,153 821,153 775,73 821,-7 913,-7"/>
    </g>
    <g role="img" aria-label="Photo: family walking through a sunny meadow">
      <polygon fill="url(#meadow-walk)" points="1119,160 1073,240 981,240 935,160 981,80 1073,80"/>
    </g>
    <g role="img" aria-label="Photo: hands around a small flower in soft light">
      <polygon fill="url(#flower-light)" points="1272,73 1226,153 1134,153 1088,73 1134,-7 1226,-7"/>
    </g>
    <g role="img" aria-label="Photo: woman receiving a relaxing head massage">
      <polygon fill="url(#massage-calm)" points="959,247 913,327 821,327 775,247 821,167 913,167"/>
    </g>
    <g role="img" aria-label="Photo: traveller in a red jacket in warm evening light">
      <polygon fill="url(#autumn-glow)" points="1272,247 1226,327 1134,327 1088,247 1134,167 1226,167"/>
    </g>
    <g role="img" aria-label="Photo: smiling hiker with a backpack in a misty forest">
      <polygon fill="url(#jungle-hike)" points="799,340 753,420 661,420 615,340 661,260 753,260"/>
    </g>
    <g role="img" aria-label="Photo: woman meditating on a beach at sunrise">
      <polygon fill="url(#beach-sunrise)" points="1119,340 1073,420 981,420 935,340 981,260 1073,260"/>
    </g>
    <g role="img" aria-label="Photo: yoga tree pose on a rock by a mountain lake">
      <polygon fill="url(#lake-yoga)" points="959,427 913,507 821,507 775,427 821,347 913,347"/>
    </g>
    <g role="img" aria-label="Photo: basket of fresh vegetables">
      <polygon fill="url(#harvest-basket)" points="799,527 753,607 661,607 615,527 661,447 753,447"/>
    </g>
  </svg>

  <h1 class="title title-gift">gift</h1>
  <p class="title title-certificate">certificate</p>

  <ul class="fields">
    <li class="field"><span class="field-label">to</span><span class="field-line"></span></li>
    <li class="field"><span class="field-label">from</span><span class="field-line"></span></li>
    <li class="field"><span class="field-label">description</span><span class="field-line"></span></li>
    <li class="field"><span class="field-label">code</span><span class="field-line"></span></li>
    <li class="field"><span class="field-label">expiry date</span><span class="field-line"></span></li>
  </ul>

  <div class="band">
    <span class="band-brace">{</span>
    <span class="band-text">your destination for gifts which are good for your mind, body, soul &amp; <strong>our precious earth</strong></span>
    <span class="band-brace">}</span>
  </div>

  <p class="website">www.novalumaro.com.au</p>

</main>
</body>
</html>
```